KerrLow Farm

Need a nice simple clean double sided business card that has our logo and info on:
Kerr Low Farm
Martin & Felicity Kerr Low
kerrlowfarm@mailbarn.example
Martin: 1-780-555-0148
Felicity: 1-780-555-0193
Instagram @ kerrlow_farm

Contact Information for Business Card

Martin & Felicity Kerr Low kerrlowfarm@mailbarn.example Martin: 1-780-555-0148 Felicity: 1-780-555-0193

```html
<!DOCTYPE html>
<html lang="en">
<head>
<meta charset="utf-8">
<title>Kerr Low Farm — Business Card</title>
<link rel="stylesheet" href="https://fonts.googleapis.com/css2?family=Questrial&family=Arimo:wght@400&display=swap">
<style>
  :root {
    --bg: #e4e2de;
    --card: #f1f1f0;
    --card-shade: #dcdcdb;
    --green: #5a9221;
    --green-dark: #4a7a1c;
    --ink: #2b2b2b;
    --sketch: #b9bcbf;
    --sketch-dark: #9ea2a6;
  }
  * { box-sizing: border-box; margin: 0; padding: 0; }
  html, body { width: 1200px; height: 1200px; overflow: hidden; }
  body {
    background: var(--bg);
    display: flex;
    flex-direction: column;
    align-items: center;
    justify-content: center;
    gap: 60px;
  }
  .card {
    position: relative;
    width: 840px;
    height: 480px;
    background: linear-gradient(135deg, var(--card) 0%, #e9e9e8 60%, var(--card-shade) 100%);
    box-shadow: 0 10px 28px rgba(0,0,0,0.12);
    overflow: hidden;
  }
  .card__band {
    position: absolute;
    top: 0;
    width: 26px;
    height: 100%;
    background: linear-gradient(180deg, var(--green) 0%, var(--green-dark) 100%);
  }
  .card__band--left { left: 0; }
  .card__band--right { right: 0; }

  /* Logo side */
  .brand {
    position: absolute;
    inset: 0;
    display: flex;
    flex-direction: column;
    align-items: center;
    justify-content: center;
    gap: 34px;
  }
  .brand__mark {
    width: 190px;
    height: 190px;
    border: 7px solid var(--green);
    border-radius: 50%;
  }
  .brand__name {
    font-family: "Questrial", sans-serif;
    font-size: 56px;
    letter-spacing: 4px;
    color: var(--green);
    text-transform: uppercase;
  }

  /* Contact side */
  .names {
    position: absolute;
    right: 66px;
    top: 56px;
    text-align: right;
    font-family: "Questrial", sans-serif;
    text-transform: uppercase;
    letter-spacing: 3px;
    line-height: 1.1;
  }
  .names__first { font-size: 40px; color: var(--ink); }
  .names__family { font-size: 44px; color: var(--green); margin-top: 6px; }

  .farm-scene {
    position: absolute;
    left: 60px;
    top: 150px;
    width: 470px;
    height: 150px;
    background: linear-gradient(180deg, rgba(185,188,191,0.15) 0%, rgba(158,162,166,0.45) 70%, rgba(185,188,191,0.1) 100%);
    border-radius: 4px;
  }

  .contacts {
    position: absolute;
    left: 66px;
    bottom: 70px;
    list-style: none;
    font-family: "Arimo", sans-serif;
    font-size: 28px;
    color: var(--ink);
  }
  .contacts__item {
    display: flex;
    align-items: center;
    gap: 14px;
    margin-top: 8px;
  }
  .contacts__icon { width: 24px; height: 24px; flex: none; }
  .contacts__label { margin-right: 14px; }
</style>
</head>
<body>

  <section class="card card--logo">
    <div class="card__band card__band--left"></div>
    <div class="card__band card__band--right"></div>
    <div class="brand">
      <div class="brand__mark"></div>
      <div class="brand__name">Kerr Low Farm</div>
    </div>
  </section>

  <section class="card card--contact">
    <div class="card__band card__band--left"></div>
    <div class="card__band card__band--right"></div>

    <div class="names">
      <div class="names__first">Martin &amp; Felicity</div>
      <div class="names__family">Kerr Low</div>
    </div>

    <div class="farm-scene" role="img" aria-label="Pencil sketch of farm barns, silo and trees on a field"></div>

    <ul class="contacts">
      <li class="contacts__item">
        <svg class="contacts__icon" viewBox="0 0 24 24" aria-hidden="true">
          <circle cx="12" cy="12" r="10.5" fill="none" stroke="var(--green)" stroke-width="2"/>
          <rect x="6.5" y="8" width="11" height="8" fill="none" stroke="var(--green)" stroke-width="1.6"/>
          <path d="M6.5 8 L12 12.5 L17.5 8" fill="none" stroke="var(--green)" stroke-width="1.6"/>
        </svg>
        <span>kerrlowfarm@mailbarn.example</span>
      </li>
      <li class="contacts__item">
        <svg class="contacts__icon" viewBox="0 0 24 24" aria-hidden="true">
          <circle cx="12" cy="12" r="10.5" fill="none" stroke="var(--green)" stroke-width="2"/>
          <path d="M8.5 7 l2 0 l1 2.5 l-1.3 1 a6 6 0 0 0 3.3 3.3 l1 -1.3 l2.5 1 l0 2 a1.5 1.5 0 0 1 -1.5 1.5 a9 9 0 0 1 -8.5 -8.5 a1.5 1.5 0 0 1 1.5 -1.5z" fill="var(--green)"/>
        </svg>
        <span><span class="contacts__label">Martin</span>1-780-555-0148</span>
      </li>
      <li class="contacts__item">
        <svg class="contacts__icon" viewBox="0 0 24 24" aria-hidden="true">
          <circle cx="12" cy="12" r="10.5" fill="none" stroke="var(--green)" stroke-width="2"/>
          <path d="M8.5 7 l2 0 l1 2.5 l-1.3 1 a6 6 0 0 0 3.3 3.3 l1 -1.3 l2.5 1 l0 2 a1.5 1.5 0 0 1 -1.5 1.5 a9 9 0 0 1 -8.5 -8.5 a1.5 1.5 0 0 1 1.5 -1.5z" fill="var(--green)"/>
        </svg>
        <span><span class="contacts__label">Felicity</span>1-780-555-0193</span>
      </li>
    </ul>
  </section>

</body>
</html>
```